Company Employee Onboarding Presentation

We need a custom PowerPoint design for a company presentation. This presentation will be sent to new employees during their onboarding/hiring process. We have attached a current mock-up of the presentation - but this is for content only. We do not like the style of the mock-up. We're a commercial real estate investment company based in Los Angeles, CA. Our website is: www.thequillmrk.com.

One artistic element that we want in the presentation is that we want a timeline similar to the attached file, but want to overlay a rising bar chart from left to right that shows the total number of units owned rising through the years. We would like this to be in the background though by using a low opacity value for the color of the graph. A great example of what we want the timeline to look like is at the bottom of the following webpage (we would just need to add the rising bar chart in the background). https://www.tollmeridecap.com/firm. This timeline is what would take the place of page 4 of the attached PP presentation.

In addition to our company landing page, the following website is representative of a style we like: https://www.vak.com

```html
<!DOCTYPE html>
<html lang="en">
<head>
<meta charset="utf-8">
<title>The Quill Group – Onboarding Deck</title>
<link href="https://fonts.googleapis.com/css2?family=Montserrat:ital,wght@0,300;0,400;0,600;0,700;1,600;1,700&display=swap" rel="stylesheet">
<style>
:root{
  --red:#c41e2e;
  --ink:#222222;
  --grey:#7d7d7d;
  --grey-panel:#858585;
  --band:#e3e3e3;
  --paper:#fafafa;
  --canvas:#ffffff;
}
*{box-sizing:border-box;margin:0;padding:0}
html,body{width:1200px;height:1200px;overflow:hidden;background:var(--canvas);font-family:'Montserrat',sans-serif;color:var(--ink)}
.board{position:relative;width:1200px;height:1200px}
.slide{position:absolute;width:325px;height:183px;background:var(--paper);box-shadow:0 4px 14px rgba(0,0,0,.22);overflow:hidden}
.c1{left:61px}.c2{left:441px}.c3{left:822px}
.r1{top:46px}.r2{top:279px}.r3{top:512px}.r4{top:745px}.r5{top:978px}
.abs{position:absolute}

.pager{position:absolute;top:16px;right:16px;width:29px;height:3px;background:#e6e6e6}
.pager::before{content:"";position:absolute;left:0;top:0;width:11px;height:3px;background:var(--red)}
.pager.light{background:rgba(255,255,255,.35)}
.pager.light::before{background:#fff}

.footer{position:absolute;left:16px;right:16px;bottom:7px;height:5px;font-size:3px;color:var(--grey);display:flex;justify-content:space-between;align-items:center}
.footer .brand{font-weight:600;color:var(--ink);font-size:3.2px}
.footer.onred{color:rgba(255,255,255,.55)}

.title{position:absolute;left:16px;top:9px;font-size:14.5px;font-weight:400;color:var(--red);letter-spacing:.1px;white-space:nowrap}
.title b{font-weight:700;color:var(--ink)}
.fine{font-size:2.6px;line-height:1.35;color:#444;text-align:justify}
.fine i{font-weight:700}

/* cover */
.cover-panel{position:absolute;left:0;top:33px;width:138px;height:117px;background:var(--grey-panel);padding:9px 0 0 19px;color:#fff}
.cover-panel.red{background:var(--red)}
.cover-brand{font-size:12px;font-weight:400;color:var(--ink);letter-spacing:-.2px}
.cover-panel.red .cover-brand{color:#fff}
.cover-tag{font-size:2.8px;font-weight:600;margin-top:2px}
.cover-title{font-size:12.5px;font-weight:300;line-height:1.3;margin-top:12px;color:var(--ink)}
.cover-panel.red .cover-title{color:#fff}
.cover-sub{font-size:3.3px;margin-top:9px;opacity:.85;color:#444}
.cover-panel.red .cover-sub{color:#fff}
.cover-photo{position:absolute;left:138px;top:33px;width:187px;height:117px;background:linear-gradient(180deg,#bcd1e6 0%,#e8edf2 45%,#d7d4cc 70%,#8e9a6e 100%)}
.cover-url{position:absolute;left:0;right:0;bottom:5px;text-align:center;font-size:3px;letter-spacing:1.2px;color:var(--grey)}

/* who */
.who-text{position:absolute;left:19px;top:52px;width:90px}
.who-red{position:absolute;left:117px;top:49px;width:91px;height:89px;background:var(--red);padding:5px 5px}
.who-red p,.who-col p{font-size:2.8px;line-height:1.3;color:#fff;margin-bottom:2.5px}
.who-red p b,.who-col p b{display:block;font-size:3px}
.who-col{position:absolute;left:213px;top:49px;width:94px;height:89px;border-left:.6px solid #999;border-bottom:.6px solid #999;padding:4px 5px}
.who-col p{color:#333}

/* business lines */
.biz{position:absolute;top:45px;width:85px}
.biz-img{height:39px;position:relative}
.biz-name{position:absolute;left:3px;bottom:2px;color:#fff;font-weight:700;font-size:7px;letter-spacing:-.2px}
.biz .fine{margin-top:3px}

/* timeline */
.band{position:absolute;left:0;right:0;top:89px;height:13px;background:repeating-linear-gradient(90deg,var(--band) 0 15px,#fff 15px 16px);border-top:.5px solid #d4d4d4;border-bottom:.5px solid #d4d4d4}
.year{position:absolute;top:79px;width:32px;height:32px;background:var(--red);color:#fff;font-size:6px;display:flex;align-items:center;justify-content:center;border:2px solid #fff;outline:.6px solid #d6d6d6;box-shadow:0 1px 4px rgba(0,0,0,.25)}
.story{position:absolute}
.story h4{font-size:4.2px;font-style:italic;font-weight:700;color:var(--red);margin-bottom:.5px}
.story.right h4{text-align:right}
.leader{position:absolute;border-color:var(--red);border-style:solid;border-width:0}

/* multi-year timeline */
.bars rect{fill:#e9e9e9}
.tag{position:absolute;font-size:2.9px;line-height:1.25;color:#555}
.tick{position:absolute;border:0 solid var(--red)}

/* now */
.stat{position:absolute;top:61px;width:39px;text-align:center}
.stat-box{width:39px;height:39px;border:.7px solid #c9c9c9;display:flex;align-items:center;justify-content:center;background:#fff}
.stat-box.on{background:var(--red);border-color:var(--red)}
.stat-label{font-size:2.9px;color:var(--grey);margin-top:3px;line-height:1.2;height:11px}
.stat-val{font-size:7.5px;color:var(--red);line-height:1.15}

/* portfolio */
.slide.red{background:var(--red)}
.title.onred{color:#fff}
.map-area{position:absolute;left:64px;top:45px;width:194px;height:116px;background:linear-gradient(160deg,#f3f3f3 0%,#e9d4d6 100%);border-radius:30px 40px 18px 60px}

/* tomorrow */
.t-panel{position:absolute;left:0;top:0;width:122px;height:183px;background:var(--red)}
.t-head{position:absolute;left:18px;top:100px;font-size:13.5px;line-height:1.1;color:var(--ink);font-weight:300}
.t-head b{display:block;color:#fff;font-weight:700}
.t-body{position:absolute;left:136px;top:33px;width:165px}
.t-body p{margin-bottom:3px}
.t-body p b{color:#222}
.t-body p.lead b{color:var(--red)}

/* values */
.v-head{position:absolute;left:17px;top:65px;font-size:14px;line-height:1.05;color:var(--red);font-weight:400}
.v-head b{display:block;color:var(--ink);font-weight:700}
.cell{position:absolute;width:45px;height:45px;display:flex;align-items:center;justify-content:center;text-align:center;font-size:3.4px;line-height:1.3;color:var(--grey);padding:3px;background:#fff;border-right:.5px solid #ddd;border-bottom:.5px solid #ddd}
.cell.on{background:var(--red);color:#fff;border-color:var(--red)}
.cell i{font-weight:600;color:#333}
</style>
</head>
<body>
<div class="board">

<!-- 1 cover grey -->
<section class="slide c1 r1">
  <div class="pager"></div>
  <div class="cover-panel">
    <div class="cover-brand">The Quill Group</div>
    <div class="cover-tag" style="color:var(--red)">Providing innovative housing solutions nationwide.</div>
    <div class="cover-title">Your<br>presentation<br>title goes here</div>
    <div class="cover-sub">Your subtitle presentation goes here</div>
  </div>
  <div class="cover-photo" role="img" aria-label="Photo of a modern white apartment building under a blue sky"></div>
  <div class="cover-url">www.thequillmrk.com</div>
</section>

<!-- 2 cover red -->
<section class="slide c2 r1">
  <div class="pager"></div>
  <div class="cover-panel red">
    <div class="cover-brand">The Quill Group</div>
    <div class="cover-tag">Providing innovative housing solutions nationwide.</div>
    <div class="cover-title">Your<br>presentation<br>title goes here</div>
    <div class="cover-sub">Your subtitle presentation goes here</div>
  </div>
  <div class="cover-photo" role="img" aria-label="Photo of a modern white apartment building under a blue sky"></div>
  <div class="cover-url">www.thequillmrk.com</div>
</section>

<!-- 3 who we are -->
<section class="slide c3 r1">
  <div class="pager"></div>
  <h2 class="title" style="top:15px;left:20px">Who <b>We Are</b></h2>
  <div class="who-text fine" style="font-size:3px;color:#777">
    The Quill Group develops and invests nationally in quality real estate projects across multiple business lines. We approach business through an entrepreneurial lens, cultivating a team who acts entrepreneurially and rewards team members commensurate with their contributions. This approach drives us to produce outsized returns.<br><br>
    While what we do determines our day-to-day, it's what we believe that makes us The Quill Group.
  </div>
  <div class="who-red">
    <p><b>We believe in being action oriented.</b>Results are achieved by compressing the distance between good ideas and great execution.</p>
    <p><b>We believe in big goals.</b>In order to achieve uncommon results, our goals must push us out of our comfort zone, beyond what we think is possible.</p>
    <p><b>We believe work and fun are not mutually exclusive.</b>When done right, hard work can be a lot of fun.</p>
  </div>
  <div class="who-col">
    <p><b>We believe in authenticity.</b>It doesn't take a suit and tie to solve big problems. Work hard and be yourself.</p>
    <p><b>We believe we can do well while doing good.</b>We give back to our communities and aim to have a lasting social impact.</p>
    <p><b>We believe in a thoughtful approach.</b>We utilize our experience and a considered approach to make swift, reasoned and forward-thinking decisions.</p>
  </div>
  <div class="footer"><span class="brand">The Quill Group</span><span>Confidential</span><span>page | 3</span></div>
</section>

<!-- 4 business lines -->
<section class="slide c1 r2">
  <div class="pager"></div>
  <h2 class="title" style="top:14px;left:19px">Our <b>Business Lines</b></h2>
  <div class="biz" style="left:18px">
    <div class="biz-img" role="img" aria-label="Photo of a worker cutting wood on a job site" style="background:linear-gradient(160deg,#e9e2da,#b98a6a 60%,#7d5a46)"><div class="biz-name">Quill Capital</div></div>
    <p class="fine">Quill Capital is the firm's market rate investment vehicle founded on the basis of value investing. Focusing on distressed opportunistic, value-add and niche market real estate assets, we target underperforming properties requiring significant renovation and hands-on management to realize their full potential.<br><br>We constantly assess market conditions and end-user demand in order to identify short and long term inefficiencies and arbitrage opportunities, applying a methodical approach to the stage for realizing superior returns.</p>
  </div>
  <div class="biz" style="left:120px">
    <div class="biz-img" role="img" aria-label="Photo of brick apartment buildings with trees" style="background:linear-gradient(170deg,#8ea4b8,#9b6a52 55%,#5f6e4a)"><div class="biz-name">Quill Communities</div></div>
    <p class="fine">In the context of a deepening affordability crisis, the group entered affordable housing in 2013 with the establishment of Quill Communities, a developer, owner and operator focused on preserving affordable housing nationwide.<br><br>Through property-based subsidies, low income housing tax credits and additional programs, we aim to preserve and expand long term housing affordability for low income households. We have a proven track record in the industry for safeguarding and growing the number of affordable units throughout the country.</p>
  </div>
  <div class="biz" style="left:221px">
    <div class="biz-img" role="img" aria-label="Photo of a row of new townhouses" style="background:linear-gradient(170deg,#a8b5c2,#6f5a4e 50%,#4b5a3c)"><div class="biz-name">Quill Impact</div></div>
    <p class="fine">Quill Impact Housing was founded to address the housing problem for middle income earners, moderate income individuals that cannot afford to reside in the communities in which they work.<br><br>Drawing upon the company's affordable and market rate housing expertise, Quill Impact Housing creates quality, income restricted housing units serving middle-income residents whose incomes exceed traditional thresholds yet remain burdened, through strategic public-private partnerships with government agencies and financial institutions.</p>
  </div>
  <div class="footer"><span class="brand">The Quill Group</span><span>Confidential</span><span>page | 4</span></div>
</section>

<!-- 5 multi-year history -->
<section class="slide c2 r2">
  <div class="pager"></div>
  <h2 class="title" style="top:9px">Company <b>History</b></h2>
  <svg class="abs bars" style="left:0;top:0" width="325" height="183" viewBox="0 0 325 183" aria-hidden="true">
    <rect x="48" y="110" width="14" height="40" opacity=".7"/>
    <rect x="74" y="104" width="14" height="46" opacity=".7"/>
    <rect x="100" y="96" width="14" height="58" opacity=".7"/>
    <rect x="126" y="84" width="14" height="70" opacity=".7"/>
    <rect x="152" y="76" width="14" height="80" opacity=".7"/>
    <rect x="178" y="66" width="14" height="92" opacity=".7"/>
    <rect x="204" y="56" width="14" height="104" opacity=".7"/>
    <rect x="230" y="46" width="14" height="116" opacity=".7"/>
    <rect x="256" y="36" width="14" height="124" opacity=".7"/>
    <rect x="282" y="26" width="14" height="132" opacity=".7"/>
    <path d="M46 118 C110 148,170 128,214 96 S262 60,268 54" fill="none" stroke="#c41e2e" stroke-opacity=".35" stroke-width="7" stroke-linecap="round"/>
    <path d="M258 46 L276 48 L266 62 Z" fill="#c41e2e" fill-opacity=".45"/>
  </svg>
  <div class="band"></div>
  <div class="year" style="left:24px">2010</div>
  <div class="year" style="left:86px">2013</div>
  <div class="year" style="left:147px">2016</div>
  <div class="year" style="left:209px">2019</div>
  <div class="year" style="left:270px">2022</div>

  <div class="tick" style="left:40px;top:42px;height:37px;width:5px;border-left-width:.5px;border-top-width:.5px"></div>
  <div class="tag" style="left:48px;top:40px">Founding</div>
  <div class="tick" style="left:60px;top:61px;height:18px;width:4px;border-left-width:.5px;border-top-width:.5px"></div>
  <div class="tag" style="left:66px;top:58px">Win Market<br>Lorem ipsum is<br>simply</div>
  <div class="tick" style="left:102px;top:38px;height:41px;width:5px;border-left-width:.5px;border-top-width:.5px"></div>
  <div class="tag" style="left:108px;top:36px">Affordable<br>housing Market<br>Lorem</div>
  <div class="tag" style="left:140px;top:68px">2000+ Market<br>Lorem ipsum is</div>
  <div class="tick" style="left:180px;top:46px;height:33px;width:5px;border-left-width:.5px;border-top-width:.5px"></div>
  <div class="tag" style="left:186px;top:35px">Market Lorem<br>ipsum is simply<br>dummy text of the<br>printing and<br>typesetting</div>
  <div class="tag" style="left:194px;top:69px">4000+ Market<br>Lorem ipsum is</div>
  <div class="tick" style="left:262px;top:40px;height:39px;width:5px;border-left-width:.5px;border-top-width:.5px"></div>
  <div class="tag" style="left:268px;top:38px">Modus Quill<br>Income Market<br>Lorem ipsum</div>
  <div class="tag" style="left:248px;top:68px">6000+ Market<br>Lorem ipsum is</div>
  <div class="tick" style="left:284px;top:56px;height:23px;width:4px;border-left-width:.5px;border-top-width:.5px"></div>
  <div class="tag" style="left:290px;top:54px">First Quill<br>Market Lorem<br>ipsum is<br>simply<br>dummy text</div>

  <div class="tick" style="left:40px;top:111px;height:14px;width:5px;border-left-width:.5px;border-bottom-width:.5px"></div>
  <div class="tag" style="left:47px;top:120px">Market Lorem<br>ipsum is simply<br>dummy text of<br>the printing and<br>typesetting<br>industry.</div>
  <div class="tag" style="left:82px;top:120px">First Market<br>Lorem</div>
  <div class="tick" style="left:124px;top:111px;height:8px;width:4px;border-left-width:.5px;border-bottom-width:.5px"></div>
  <div class="tag" style="left:126px;top:116px">First Quill<br>Market Lorem<br>ipsum is simply<br>dummy text</div>
  <div class="tick" style="left:225px;top:111px;height:22px;width:4px;border-left-width:.5px;border-bottom-width:.5px"></div>
  <div class="tag" style="left:231px;top:135px">Quill Market<br>Lorem<br>challenge is<br>simple dummy<br>text</div>
  <div class="tick" style="left:286px;top:111px;height:8px;width:4px;border-left-width:.5px;border-bottom-width:.5px"></div>
  <div class="tag" style="left:264px;top:116px">First Quill<br>Market Lorem<br>ipsum is simply<br>dummy text</div>
  <div class="footer"><span class="brand">The Quill Group</span><span>Confidential</span><span>page | 5</span></div>
</section>

<!-- 6 history 2010-2011 -->
<section class="slide c3 r2">
  <div class="pager"></div>
  <h2 class="title" style="top:9px">Company <b>History</b></h2>
  <div class="band"></div>
  <div class="year" style="left:28px">2010</div>
  <div class="year" style="left:245px">2011</div>
  <div class="leader" style="left:44px;top:58px;width:14px;height:21px;border-left-width:.5px;border-top-width:.5px"></div>
  <div class="story" style="left:58px;top:42px;width:183px">
    <h4>What do you get when you combine a principal, an unpaid intern, and 5,000 square feet of borrowed office space? The beginning of Quill</h4>
    <p class="fine">In 2010, we found the company based on value investing principles in the depths of the financial crisis with a focus on value-add, distressed and opportunistic investments. We leverage our significant experience and track record in the value-add space, starting small and building an investment firm from the ground up. It may not be the easiest path to choose, but <i>we do what's right and not what's easy.</i></p>
  </div>
  <div class="leader" style="left:44px;top:111px;width:14px;height:14px;border-left-width:.5px;border-bottom-width:.5px"></div>
  <div class="story" style="left:58px;top:120px;width:183px">
    <h4>Start with what you know</h4>
    <p class="fine">Finding a hidden gem, polishing it, and presenting it to the world can be a lot of fun. We know how to do it and enjoy doing it, so we decide to dive into the value-add apartment business. We find the worn out properties in great neighborhoods and the underutilized properties in the next hot neighborhoods. The key to success is to see things for what they can be, and not just what they are, then to <i>innovate through reimagining, reorganizing and reworking.</i></p>
  </div>
  <div class="footer"><span class="brand">The Quill Group</span><span>Confidential</span><span>page | 6</span></div>
</section>

<!-- 7 history 2011-2012 -->
<section class="slide c1 r3">
  <div class="pager"></div>
  <h2 class="title" style="top:9px">Company <b>History</b></h2>
  <div class="band"></div>
  <div class="year" style="left:29px">2011</div>
  <div class="year" style="left:245px">2012</div>
  <div class="leader" style="left:45px;top:38px;width:15px;height:41px;border-left-width:.5px;border-top-width:.5px"></div>
  <div class="story" style="left:59px;top:34px;width:152px">
    <h4>Who wouldn't want to buy $1.00 for 70 cents?</h4>
    <p class="fine">Armed with a man at the court house steps with an ear pod in one ear and millions of dollars of cashier checks in his back pocket, we embark on a daily ritual of bidding on apartment building foreclosures. Through the Ridgeway Opportunity Fund, a discretionary investment fund we raise to bid on foreclosed and distressed apartments, we successfully invest in this space over a four year period. With no traditional diligence available for the properties and just seconds to bid, it can be a nerve wracking experience, but we never lose money on any of the acquisitions and actually earn quite an attractive return. If this isn't a crash course in <i>making swift, reasoned, and forward thinking decisions</i>, we don't know what is.</p>
  </div>
  <div class="footer"><span class="brand">The Quill Group</span><span>Confidential</span><span>page | 7</span></div>
</section>

<!-- 8 history 2012-2013 -->
<section class="slide c2 r3">
  <div class="pager"></div>
  <h2 class="title" style="top:9px">Company <b>History</b></h2>
  <div class="band"></div>
  <div class="year" style="left:29px">2012</div>
  <div class="year" style="left:246px">2013</div>
  <div class="leader" style="left:45px;top:46px;width:10px;height:33px;border-left-width:.5px;border-top-width:.5px"></div>
  <div class="story" style="left:55px;top:42px;width:125px">
    <h4>Eureka!</h4>
    <p class="fine">After a nail biting 22 months of money going out the door during the company's initial existence, we successfully complete our first disposition of an investment which (thankfully) brings some profit back into the bank account. With a sale price 55% above our purchase, we're off to a good start. And better yet, our investment thesis is validated.</p>
  </div>
  <div class="leader" style="left:252px;top:111px;width:10px;height:14px;border-right-width:.5px;border-bottom-width:.5px"></div>
  <div class="story right" style="left:90px;top:120px;width:162px">
    <h4>Doing well while doing good.</h4>
    <p class="fine">After rigorous analysis we dip our toe in the affordable housing waters because of perceived opportunity. While the initial opportunity is just a sliver of the vast affordable housing landscape we uncover in the years to come, the affordable industry becomes more of a mission rather than just a mere opportunity. We create a new segment of the business, Quill Communities, to focus on fulfilling affordable housing needs across the country. This would not be possible without <i>our pursuit of lifelong learning</i>, allowing us to marry our existing multifamily experience with a new asset class.</p>
  </div>
  <div class="footer"><span class="brand">The Quill Group</span><span>Confidential</span><span>page | 8</span></div>
</section>

<!-- 9 history 2015-2016 -->
<section class="slide c3 r3">
  <div class="pager"></div>
  <h2 class="title" style="top:9px">Company <b>History</b></h2>
  <div class="band"></div>
  <div class="year" style="left:28px">2015</div>
  <div class="year" style="left:245px">2016</div>
  <div class="leader" style="left:44px;top:46px;width:12px;height:33px;border-left-width:.5px;border-top-width:.5px"></div>
  <div class="story" style="left:56px;top:42px;width:92px">
    <h4>Ladies and gentlemen, start your engines.</h4>
    <p class="fine">While the debate still rages in the office as to who actually won the inaugural Quill go karting race, one thing is certain: we all walk away that day with big smiles on our faces. <i>We work hard and have fun</i>, otherwise, what's the point?</p>
  </div>
  <div class="leader" style="left:252px;top:111px;width:10px;height:14px;border-right-width:.5px;border-bottom-width:.5px"></div>
  <div class="story right" style="left:82px;top:118px;width:170px">
    <h4>The Naked City</h4>
    <p class="fine">Just off the glittering Las Vegas strip we find what we believe to be an attractive affordable housing opportunity. But once we complete our diligence, we realize that the property has too many physical needs to be a viable long term investment. Rather than walking away, we decide to dive deeper into the affordable housing world by utilizing the Low Income Housing Tax Credit to complete a redevelopment of the 201 unit property located in a neighborhood known as The Naked City for its history as a home to many of the city's showgirls in the 50's and 60's. This redevelopment not only enhances the lives of the residents, but contributes to lifting the entire neighborhood. This is the first of many projects Quill Communities undertakes to redevelop affordable housing across the country.</p>
  </div>
  <div class="footer"><span class="brand">The Quill Group</span><span>Confidential</span><span>page | 9</span></div>
</section>

<!-- 10 history 2019-2020 -->
<section class="slide c1 r4">
  <div class="pager"></div>
  <h2 class="title" style="top:9px">Company <b>History</b></h2>
  <div class="band"></div>
  <div class="year" style="left:29px">2019</div>
  <div class="year" style="left:245px">2020</div>
  <div class="leader" style="left:45px;top:41px;width:10px;height:38px;border-left-width:.5px;border-top-width:.5px"></div>
  <div class="story" style="left:55px;top:38px;width:177px">
    <h4>46..., 47..., 48...., 49....., 50!</h4>
    <p class="fine">Never are we met with such a range of emotions for a company activity: excitement, nervousness, dread. The Quill health challenge is a 60 day competition that tests our willpower, establishes beneficial habits, and leaves us feeling a better version of ourselves. We gain points by simply eating right and working out, all while having a trainer cheering us along or giving us a nudge. Our single biggest competitor is ourself. To be successful, <i>we must approach each day with intention</i>, just like we approach our business. A testament to the spirit of the team, the competition is neck and neck until the very end.</p>
  </div>
  <div class="leader" style="left:252px;top:111px;width:10px;height:14px;border-right-width:.5px;border-bottom-width:.5px"></div>
  <div class="story right" style="left:85px;top:120px;width:167px">
    <h4>Solving for the missing middle</h4>
    <p class="fine">How can we have thriving cities when the people who work and play there cannot afford to live there? Spoiler alert: we can't. Expensive, high-end housing pencils to build. Affordable housing for low income renters, although scarce, can pencil to build through government funded programs. But what about middle income renters who make the cities run? They are left with dilapidated, old housing stock, or spending hours a day fighting traffic to get to and from work. <i>Harnessing the collective and collaborative power of a public/private team</i>, Quill Impact Housing is born to address this crucial need, providing high quality housing to the teachers, nurses, and professionals who are the lifeblood of our cities.</p>
  </div>
  <div class="footer"><span class="brand">The Quill Group</span><span>Confidential</span><span>page | 10</span></div>
</section>

<!-- 11 history 2021-2022 -->
<section class="slide c2 r4">
  <div class="pager"></div>
  <h2 class="title" style="top:9px">Company <b>History</b></h2>
  <div class="band"></div>
  <div class="year" style="left:29px">2021</div>
  <div class="year" style="left:246px">2022</div>
  <div class="leader" style="left:45px;top:48px;width:10px;height:31px;border-left-width:.5px;border-top-width:.5px"></div>
  <div class="story" style="left:55px;top:44px;width:122px">
    <h4>Movin' on up</h4>
    <p class="fine">The growth and success of a company does not happen overnight, nor does it just happen. It takes a team of dedicated, intelligent, results oriented individuals to deliver exceptional results. When a member of the team consistently delivers results, <i>we reward those results</i>. In this case, we name our first Partner.</p>
  </div>
  <div class="leader" style="left:252px;top:111px;width:10px;height:14px;border-right-width:.5px;border-bottom-width:.5px"></div>
  <div class="story right" style="left:125px;top:120px;width:127px">
    <h4>Don't step in the kitchen</h4>
    <p class="fine">What company retreat is complete without a bit of work, a lot of laughs, and little competition? The competitive juices are in full swing at the first Quill pickleball tournament. The open courtside bar soothes the sting of defeat, but regardless of where we each rank in the standings, there is a lot of talk of pickleball becoming the new favorite Quill pastime.</p>
  </div>
  <div class="footer"><span class="brand">The Quill Group</span><span>Confidential</span><span>page | 11</span></div>
</section>

<!-- 12 where are we now -->
<section class="slide c3 r4">
  <div class="pager"></div>
  <h2 class="title" style="top:15px;left:20px">Where Are <b>We Now</b></h2>
  <div class="stat" style="left:16px">
    <div class="stat-box"><svg width="18" height="16" viewBox="0 0 18 16"><g fill="#c41e2e"><rect x="1" y="6" width="5" height="10"/><rect x="7" y="2" width="5" height="14"/><rect x="13" y="5" width="4" height="11"/></g></svg></div>
    <div class="stat-label">Apartment Units<br>Acquired</div><div class="stat-val">7,500 +</div>
  </div>
  <div class="stat" style="left:66px">
    <div class="stat-box"><svg width="18" height="14" viewBox="0 0 18 14"><g fill="#c41e2e"><circle cx="9" cy="3" r="2.6"/><circle cx="3.5" cy="5" r="2"/><circle cx="14.5" cy="5" r="2"/><rect x="5" y="7" width="8" height="6" rx="2"/><rect x="0.5" y="8" width="6" height="5" rx="2"/><rect x="11.5" y="8" width="6" height="5" rx="2"/></g></svg></div>
    <div class="stat-label">Senior Management<br>Team Acquisition<br>Experience</div><div class="stat-val">Over $4<br>billion</div>
  </div>
  <div class="stat" style="left:114px">
    <div class="stat-box"><svg width="13" height="16" viewBox="0 0 13 16"><rect x="1" y="1" width="11" height="14" fill="none" stroke="#c41e2e" stroke-width="1.2"/><path d="M3 5h7M3 8h7M3 11h4" stroke="#c41e2e" stroke-width="1"/></svg></div>
    <div class="stat-label">Current Assets<br>Under Management</div><div class="stat-val">$1+ billion</div>
  </div>
  <div class="stat" style="left:164px">
    <div class="stat-box on"><svg width="18" height="14" viewBox="0 0 18 14"><g fill="#fff"><rect x="1" y="4" width="2" height="9"/><rect x="5" y="4" width="2" height="9"/><rect x="9" y="4" width="2" height="9"/><rect x="13" y="4" width="2" height="9"/><rect x="0" y="1" width="17" height="2"/></g></svg></div>
    <div class="stat-label">Number of<br>Residents Served</div><div class="stat-val">13,000+</div>
  </div>
  <div class="stat" style="left:214px">
    <div class="stat-box"><svg width="14" height="16" viewBox="0 0 14 16"><g fill="#c41e2e"><path d="M2 6 A5 5 0 0 1 12 6 Z"/><rect x="1" y="6" width="12" height="1.5"/><rect x="3" y="9" width="8" height="7"/></g></svg></div>
    <div class="stat-label">Renovations<br>Performed</div><div class="stat-val">$60mm+</div>
  </div>
  <div class="stat" style="left:264px">
    <div class="stat-box"><svg width="16" height="14" viewBox="0 0 16 14"><path d="M1 1v12h14" fill="none" stroke="#c41e2e" stroke-width="1"/><path d="M3 10l4-4 3 2 4-5" fill="none" stroke="#c41e2e" stroke-width="1.2"/></svg></div>
    <div class="stat-label">IRR of Realized<br>Investments - Quill<br>Communities</div><div class="stat-val">34.87%</div>
  </div>
  <div class="footer"><span class="brand">The Quill Group</span><span>Confidential</span><span>page | 12</span></div>
</section>

<!-- 13 portfolio -->
<section class="slide red c1 r5">
  <div class="pager light"></div>
  <h2 class="title onred" style="top:16px;left:19px">Our <b>Nationwide Portfolio</b></h2>
  <div class="map-area" role="img" aria-label="Map of the United States with portfolio states highlighted in red"></div>
  <div class="footer onred"><span class="brand">The Quill Group</span><span>Confidential</span><span>page | 13</span></div>
</section>

<!-- 14 tomorrow -->
<section class="slide c2 r5">
  <div class="pager"></div>
  <div class="t-panel"></div>
  <div class="t-head">What Does<b>Tomorrow</b><b>Look Like?</b></div>
  <div class="t-body">
    <p class="fine lead" style="color:var(--red)"><b>We will be a market leader.</b> We will pursue growth and innovation to achieve industry beating returns and responsibly expand our portfolio through new and existing business lines.</p>
    <p class="fine"><b>We will positively impact those we touch.</b> We have a responsibility to create opportunity for our residents and our employees. Investing in the success of both parties, particularly by <i>empowering individuals</i>, will help us enact the social impact that is sorely needed.</p>
    <p class="fine"><b>We will have a positive impact on those we touch.</b> We will positively impact all stakeholders in our business (residents, employees, communities and investors) by adhering to a high standard in terms of both our fiduciary and social obligations.</p>
    <p class="fine">We will have a positive and lasting effect on residents and communities by doing what's right not what's easy.</p>
    <p class="fine"><b>We will reduce our footprint.</b> We recognize that the construction industry has a significant carbon footprint. Through our perpetual desire to <i>innovate through reimagining, reorganizing and reworking</i> we will find further solutions to substantially reduce it.</p>
    <p class="fine"><b>We will utilize our expertise to its fullest.</b> The multifamily industry has been one of the highest performing asset classes and is poised to remain such. We will outperform the favorable market by applying all of our experience to mitigate risk and enhance upside.</p>
  </div>
  <div class="footer"><span class="brand">The Quill Group</span><span>Confidential</span><span>page | 14</span></div>
</section>

<!-- 15 core values -->
<section class="slide c3 r5">
  <div class="pager"></div>
  <div class="v-head">Our<b>Core</b><b>Values</b></div>
  <div class="cell" style="left:155px;top:27px">We do what's right, not what's easy</div>
  <div class="cell on" style="left:201px;top:27px">We lead by example</div>
  <div class="cell" style="left:246px;top:27px">We harness the collective and collaborative power of the team</div>
  <div class="cell" style="left:111px;top:74px">We empower individuals</div>
  <div class="cell" style="left:155px;top:74px"><i>We make swift, reasoned and forward-thinking decisions</i></div>
  <div class="cell" style="left:201px;top:74px">We pursue lifelong learning</div>
  <div class="cell" style="left:246px;top:74px">We reward results</div>
  <div class="cell on" style="left:66px;top:119px">We approach each day with intention</div>
  <div class="cell" style="left:111px;top:119px">We innovate through reimagining, reorganizing and reworking</div>
  <div class="cell" style="left:155px;top:119px">We think and act like owners</div>
  <div class="cell on" style="left:201px;top:119px">We work hard and have fun</div>
  <div class="footer"><span class="brand">The Quill Group</span><span>Confidential</span><span>page | 15</span></div>
</section>

</div>
</body>
</html>
```